Preliminary design concepts for VELARIN history document

To produce three design concepts as a demonstration for the layout of a document with a look and feel compatible with the existing documents/visual identity of an Australia-based NGO. The design concepts will be used to provide concepts to the NGO and ideally select a designer for the longer 30 - 50 page document.

Target Market(s)

Australian heritage community, international heritage community, general population interested in heritage issues and key stakeholders in heritage projects

Colors
0455a3
3176b5
85acd3
ffc214
fece3e
fee18a
f78f20
f37122

Requirements
Must have
• Eye catching but authoritative design to reflect a serious professional organisation, but one which reflects a modern, progressive approach.
• The designer needs to have experience working with document layout in InDesign and/or Illustrator and provide files in a range of outputs including EPS formats as well as HTML and PDF.
Nice to have
• Interplay between images and design elements

```html
<!DOCTYPE html>
<html lang="en">
<head>
<meta charset="utf-8">
<title>Innovation in Conservation – Australia VELARIN history</title>
<link href="https://fonts.googleapis.com/css2?family=Pinyon+Script&family=Raleway:wght@300;400;600&family=Quicksand:wght@300;400&family=Open+Sans:wght@400;600&display=swap" rel="stylesheet">
<style>
  :root {
    --backdrop: #d4d3d9;
    --paper: #ffffff;
    --charcoal: #3b3b3d;
    --ink: #2a2a2a;
    --body-ink: #555555;
    --orange: #f37122;
    --orange-bright: #f78f20;
    --orange-deep: #b4531c;
  }
  * { margin: 0; padding: 0; box-sizing: border-box; }
  html, body { width: 1200px; height: 768px; overflow: hidden; background: var(--backdrop); }
  .canvas { position: relative; width: 1200px; height: 768px; }

  /* Cover */
  .cover {
    position: absolute; left: 163px; top: 175px; width: 258px; height: 405px;
    background: var(--paper); overflow: hidden;
    box-shadow: 0 6px 14px rgba(0,0,0,.18);
  }
  .cover__top-band { position: absolute; left: 0; top: 0; width: 100%; height: 52px; background: var(--charcoal); }
  .cover__side-band { position: absolute; right: 0; top: 0; width: 50px; height: 292px; background: var(--charcoal); }
  .cover__title { position: absolute; left: 6px; top: 56px; width: 246px; }
  .cover__title-script {
    font-family: "Pinyon Script", cursive; font-size: 34px; color: var(--ink); line-height: 1;
  }
  .cover__title-main {
    font-family: "Raleway", sans-serif; font-weight: 300; font-size: 25px; letter-spacing: .3px;
    color: var(--orange); line-height: 1; margin-top: -4px; padding-left: 28px; white-space: nowrap;
  }
  .cover__subtitle {
    position: absolute; left: 0; top: 121px; width: 258px; height: 14px;
    background: #1f1f1f; color: #fff;
    font-family: "Raleway", sans-serif; font-size: 8.4px; line-height: 14px; padding-left: 12px; white-space: nowrap;
  }
  .cover__photo {
    position: absolute; left: 0; top: 135px; width: 208px; height: 157px;
    background: linear-gradient(180deg, #f0f0f0 0%, #bdbdbd 30%, #6f6f6f 60%, #2e2e2e 100%);
  }
  .cover__photo-band {
    position: absolute; left: 0; top: 292px; width: 208px; height: 63px;
    background: linear-gradient(90deg, #6a2f12, var(--orange-deep) 60%, #8a3b15);
  }
  .cover__accent-band {
    position: absolute; left: 208px; top: 292px; width: 50px; height: 63px; background: var(--orange-bright);
  }
  .cover__brand {
    position: absolute; left: 10px; top: 373px;
    font-family: "Raleway", sans-serif; font-weight: 400; font-size: 9px; color: var(--charcoal); letter-spacing: .3px;
  }

  /* Spread */
  .spread {
    position: absolute; left: 503px; top: 172px; width: 524px; height: 408px;
    background: var(--paper); overflow: hidden;
    box-shadow: 0 6px 14px rgba(0,0,0,.18);
  }
  .spread__photo {
    position: absolute; left: 0; top: 0; width: 331px; height: 100%;
    background: linear-gradient(160deg, #8a8a8a 0%, #e2e2e2 25%, #5a5a5a 50%, #cfcfcf 72%, #2c2c2c 100%);
  }
  .spread__gutter {
    position: absolute; left: 262px; top: 0; width: 10px; height: 100%;
    background: linear-gradient(90deg, rgba(0,0,0,.25), rgba(0,0,0,0));
  }
  .spread__overlay {
    position: absolute; left: 0; top: 86px; width: 331px; height: 264px;
    background: linear-gradient(90deg, rgba(150,62,18,.86), rgba(200,96,40,.8) 60%, rgba(120,50,16,.85));
  }
  .spread__statement {
    position: absolute; left: 22px; top: 120px; width: 250px;
    font-family: "Quicksand", sans-serif; font-weight: 400; font-size: 16.5px; line-height: 21px;
    text-transform: uppercase; color: #fff; letter-spacing: .3px;
  }
  .spread__text {
    position: absolute; left: 338px; top: 44px; width: 180px;
    font-family: "Open Sans", sans-serif; color: var(--body-ink);
  }
  .spread__heading {
    font-family: "Quicksand", sans-serif; font-weight: 400; font-size: 9px; line-height: 10px;
    color: var(--orange); text-transform: uppercase; margin-bottom: 26px; letter-spacing: .2px;
  }
  .spread__heading strong { font-weight: 600; font-family: "Raleway", sans-serif; }
  .spread__para { font-size: 4.4px; line-height: 6.6px; text-align: justify; margin-bottom: 6px; }
</style>
</head>
<body>
<div class="canvas">

  <section class="cover">
    <div class="cover__top-band"></div>
    <div class="cover__side-band"></div>
    <div class="cover__title">
      <div class="cover__title-script">Innovation in</div>
      <div class="cover__title-main">CONSERVATION</div>
    </div>
    <div class="cover__subtitle">A brief history of Australia VELARIN and the Kestrel Charter</div>
    <div class="cover__photo" role="img" aria-label="Black and white photograph of a ruined stone chimney building on a grassy hill"></div>
    <div class="cover__photo-band" role="img" aria-label="Orange-toned view of dry ground at the foot of the ruin"></div>
    <div class="cover__accent-band"></div>
    <div class="cover__brand">AUSTRALIA VELARIN</div>
  </section>

  <section class="spread">
    <div class="spread__photo" role="img" aria-label="Close-up black and white photograph of people gathered at a heritage event"></div>
    <div class="spread__gutter"></div>
    <div class="spread__overlay"></div>
    <p class="spread__statement">Since 1976 Australia VELARIN has been committed to improving conservation philosophy and practice for culturally significant places.</p>

    <div class="spread__text">
      <h2 class="spread__heading"><strong>Introduction—</strong><br>What is Australia VELARIN?</h2>
      <p class="spread__para">“The idea of our council is remarkable. It is international, professional yet independent and inter-disciplinary. Its twin tasks are to care for human creations around the world and across time and to reveal the striking messages their built fabric conveys. Thus it has the excitement of exploring the physical and reflecting upon the metaphysical.” (Mara Ellwood, 1997)</p>
      <p class="spread__para">Australia VELARIN is an incorporated association of professionals working for the conservation and protection of cultural heritage places, including buildings, historic cities, cultural landscapes and Indigenous heritage sites. Its mission is to lead cultural heritage conservation in Australia by raising standards, encouraging debate and generating innovative ideas. It plays a strong role in advancing heritage practice in Australia and in the Asia–Pacific region.</p>
      <p class="spread__para">Its parent body, VELARIN International, is one of three formal advisory bodies to the world heritage committee. It is the professional and scientific advisor to that committee on all aspects of cultural heritage, and Australia VELARIN is one of many national committees linked to it.</p>
      <p class="spread__para">Australia VELARIN became an incorporated association in 1984. It now has over six hundred members across a range of disciplines, including architects, historians, archaeologists, town planners, conservators, geographers, engineers, lawyers and academics. It is one of the largest national bodies in the network.</p>
      <p class="spread__para">Members have long played a substantial role in advancing heritage practice internationally, serving on the executive committee since 1981 and taking part in many scientific committees that meet around the globe to develop expertise on specific heritage issues.</p>
    </div>
  </section>

</div>
</body>
</html>
```